依頼詳細
購買意欲に響く電子チラシが欲しい。
記載項目
社名、情報、キャッチコピー
サイズ
A4
ページ数
片面
希望イメージ
シンプル 複雑
単色 カラフル
暗い 明るい
日常 高級
遊び心 厳粛
未来的 伝統的
女性的 男性的
希望する色
黄・オレンジ系、青系、無彩色系
納品ファイル
• 高解像度JPG (.jpg)
補足説明
販促用チラシの作成。

会員年齢層は平均40-50代が中心4000名ほど
見やすく、販促意欲を刺激するものを希望。

購入されたポイントは旅行やギフトを使えます。
会社ページ
https://www.lunafield-qz.app/

```html
<!DOCTYPE html>
<html lang="ja">
<head>
<meta charset="utf-8">
<title>1億円還元キャンペーン</title>
<link href="https://fonts.googleapis.com/css2?family=Noto+Sans+JP:wght@500;700;900&family=Noto+Serif+JP:wght@700;900&display=swap" rel="stylesheet">
<style>
:root{
  --red:#d7141e;
  --red-dark:#a80d14;
  --orange:#f39a1a;
  --yellow:#ffe23a;
  --navy:#0d2b5c;
  --sky-top:#cfe3f3;
  --sky-bottom:#f4f8fc;
  --gray:#8a8a8a;
  --ink:#1a1a1a;
  --white:#ffffff;
}
*{margin:0;padding:0;box-sizing:border-box}
html,body{width:890px;height:1200px;overflow:hidden;background:var(--white)}
body{font-family:"Noto Sans JP",sans-serif;color:var(--ink)}
.flyer{position:relative;width:890px;height:1200px;overflow:hidden}
.hero-photos{position:absolute;top:0;left:0;width:890px;height:175px;
  background:linear-gradient(90deg,#6b4a32 0%,#b98a5e 22%,#3f7fb3 45%,#7fb7de 62%,#c99a62 80%,#4a6f8f 100%)}
.skyline{position:absolute;top:175px;left:0;width:890px;height:860px;
  background:linear-gradient(180deg,var(--sky-top) 0%,#dfeaf4 45%,var(--sky-bottom) 100%)}
.badges{position:absolute;top:150px;right:40px;display:flex;gap:14px}
.badge{width:118px;height:118px;border-radius:50%;background:var(--yellow);
  border:4px solid var(--orange);display:flex;align-items:center;justify-content:center;
  text-align:center;font-weight:900;color:var(--red);font-size:22px;line-height:1.15;
  box-shadow:0 3px 6px rgba(0,0,0,.25)}
.title{position:absolute;left:40px;top:262px;font-family:"Noto Serif JP",serif;font-weight:900;color:var(--red);
  -webkit-text-stroke:2px var(--white);paint-order:stroke fill;line-height:1}
.title .amount{font-size:92px}
.title .amount small{font-size:54px}
.title .name{display:block;font-size:96px;margin-top:4px;letter-spacing:-2px}
.lead{position:absolute;left:40px;top:470px;font-weight:900;font-size:24px;line-height:1.35;color:var(--ink)}
.deadline{position:absolute;left:470px;top:482px;font-weight:900;font-size:44px;line-height:1.2;color:var(--red)}
.deadline .dow{display:inline-block;width:40px;height:40px;border-radius:50%;background:var(--red);color:var(--white);
  font-size:24px;text-align:center;line-height:40px;vertical-align:middle;margin:0 4px}
.deadline .until{font-size:34px;color:var(--ink)}
.rates{position:absolute;left:40px;top:566px;width:810px}
.rates-head{display:flex;height:36px;align-items:flex-end}
.rates-head .normal{margin-left:238px;width:92px;text-align:center;font-weight:700;font-size:18px;color:var(--gray);
  border:2px solid var(--orange);border-bottom:none;background:var(--white)}
.rates-head .campaign{margin-left:40px;width:420px;text-align:center;font-weight:900;font-size:28px;color:var(--orange)}
.rate-row{display:flex;align-items:center;height:70px;margin-bottom:10px;background:rgba(255,255,255,.88);
  border-top:2px solid var(--red);border-bottom:2px solid var(--red)}
.rate-row .yen{width:230px;height:100%;background:var(--navy);color:var(--white);font-weight:900;font-size:27px;
  display:flex;align-items:center;justify-content:center}
.rate-row .base{width:92px;margin-left:8px;height:100%;border-left:2px solid var(--orange);border-right:2px solid var(--orange);
  color:var(--gray);font-weight:700;font-size:22px;display:flex;align-items:center;justify-content:center}
.rate-row .arrow{width:50px;display:flex;justify-content:center}
.rate-row .bonus-rt{width:230px;text-align:center;color:var(--red);font-weight:900;font-size:46px;line-height:1}
.rate-row .bonus-rt small{font-size:27px}
.rate-row .boost{margin-left:auto;margin-right:10px;width:180px;height:56px;background:var(--red);color:var(--white);
  text-align:center;font-weight:900;font-size:20px;line-height:1.15;display:flex;flex-direction:column;justify-content:center}
.rate-row .boost span{font-size:12px;font-weight:500}
.footer{position:absolute;left:0;bottom:0;width:890px;height:165px;background:var(--white);text-align:center;padding-top:26px}
.footer .company{font-family:"Noto Serif JP",serif;font-weight:900;font-size:34px;color:var(--ink)}
.footer .address{font-size:15px;margin-top:4px;color:var(--ink)}
.footer .tel{font-family:"Noto Serif JP",serif;font-weight:700;font-size:28px;color:var(--red);margin-top:4px}
</style>
</head>
<body>
<main class="flyer">
  <div class="hero-photos" role="img" aria-label="リゾートホテルの客室、プール、旅客機のイメージ写真"></div>
  <div class="skyline" role="img" aria-label="高層ビルが並ぶ都市の景色"></div>

  <div class="badges">
    <div class="badge">期間<br>限定!</div>
    <div class="badge">お得!</div>
    <div class="badge">RT<br>付与率<br>UP!</div>
  </div>

  <h1 class="title"><span class="amount">1億<small>円</small></span><span class="name">還元キャンペーン</span></h1>

  <p class="lead">確定した報酬からRTに<br>変換したら通常より断然お得に!</p>
  <p class="deadline">5月31日<span class="dow">水</span><span class="until">まで</span></p>

  <section class="rates">
    <div class="rates-head"><div class="normal">通常</div><div class="campaign">キャンペーン中</div></div>

    <div class="rate-row"><div class="yen">25,000円分</div><div class="base">17.5RT</div>
      <div class="arrow"><svg width="28" height="32" viewBox="0 0 30 34"><path d="M0 0 L30 17 L0 34 Z" fill="#d7141e"/></svg></div>
      <div class="bonus-rt">18.5<small>RT</small></div><div class="boost">付与率5%UP<span>(+1RT付与)</span></div></div>

    <div class="rate-row"><div class="yen">50,000円分</div><div class="base">35RT</div>
      <div class="arrow"><svg width="28" height="32" viewBox="0 0 30 34"><path d="M0 0 L30 17 L0 34 Z" fill="#d7141e"/></svg></div>
      <div class="bonus-rt">38.5<small>RT</small></div><div class="boost">付与率10%UP<span>(+3.5RT付与)</span></div></div>

    <div class="rate-row"><div class="yen">100,000円分</div><div class="base">70RT</div>
      <div class="arrow"><svg width="28" height="32" viewBox="0 0 30 34"><path d="M0 0 L30 17 L0 34 Z" fill="#d7141e"/></svg></div>
      <div class="bonus-rt">80.5<small>RT</small></div><div class="boost">付与率15%UP<span>(+10.5RT付与)</span></div></div>

    <div class="rate-row"><div class="yen">200,000円分</div><div class="base">140RT</div>
      <div class="arrow"><svg width="28" height="32" viewBox="0 0 30 34"><path d="M0 0 L30 17 L0 34 Z" fill="#d7141e"/></svg></div>
      <div class="bonus-rt">166<small>RT</small></div><div class="boost">付与率20%UP<span>(+26RT付与)</span></div></div>

    <div class="rate-row"><div class="yen">500,000円分</div><div class="base">350RT</div>
      <div class="arrow"><svg width="28" height="32" viewBox="0 0 30 34"><path d="M0 0 L30 17 L0 34 Z" fill="#d7141e"/></svg></div>
      <div class="bonus-rt">437.5<small>RT</small></div><div class="boost">付与率25%UP<span>(+87.5RT付与)</span></div></div>
  </section>

  <footer class="footer">
    <p class="company">株式会社Luna Field QZ</p>
    <p class="address">東京都港区南青山3-8-2 ルナフィールドビル9F</p>
    <p class="tel">TEL: 050-0000-4821</p>
  </footer>
</main>
</body>
</html>
```